Retirement maintenance and reinstatment brochure

We are looking for a capability statement/brochure outlining our skills and capabilities for maintenance, reinstatement and refurbishment work specific to the requirements of retirement villages in Australia

We are a new company, however our people have significant experience working in this industry

Target Market(s)

Retirement living facilities, aged care facilities, hospitals

Industry/Entity Type

Building

Colors

Designer to choose colors to be used in the design.

Requirements
Must have
• Not alot of wording. Stock images of building refurbishment to retirement living and aged care (carpenters, painters etc)
Nice to have
• 1-2 pages only
Should not have
• alot of meaningless writing

```html
<!DOCTYPE html>
<html lang="en">
<head>
<meta charset="utf-8">
<title>Swift Care Maintenance Solutions – Capability Flyer</title>
<link href="https://fonts.googleapis.com/css2?family=Lato:wght@400;700&display=swap" rel="stylesheet">
<style>
  :root{
    --navy:#123f7a;
    --blue:#1f64ad;
    --blue-deep:#154a8c;
    --red:#d3182d;
    --ink:#333a44;
    --paper:#ffffff;
    --stage:#e9ebee;
    --mist:#eef0f3;
  }
  *{box-sizing:border-box;margin:0;padding:0}
  html,body{width:1200px;height:1200px;overflow:hidden;background:var(--stage)}
  body{position:relative;font-family:'Lato',sans-serif;color:var(--ink)}
  .flyer{position:absolute;left:190px;top:25px;width:820px;height:1150px;background:var(--paper);overflow:hidden;box-shadow:0 6px 24px rgba(0,0,0,.18)}
  .flyer svg{position:absolute;left:0;top:0}
  .brand{position:absolute;left:40px;top:70px;display:flex;align-items:center;gap:14px}
  .brand-dot{width:70px;height:70px;border-radius:50%;background:var(--blue)}
  .brand-name{font-family:'Lato',sans-serif;font-weight:700;font-size:30px;color:var(--navy);line-height:1.1;width:300px}
  .about{position:absolute;left:34px;top:598px;width:360px}
  .about h2{font-size:20px;font-weight:700;color:var(--navy);line-height:1.1}
  .about p{font-size:13.6px;line-height:1.25;text-align:justify}
  .about .lead{margin-bottom:12px}
  .trades{position:absolute;left:34px;top:788px;width:360px}
  .trades h3{font-size:20px;font-weight:700;color:var(--navy);margin-bottom:2px}
  .trades ul{list-style:none}
  .trades li{font-size:13.4px;line-height:16.2px;padding-left:12px;position:relative}
  .trades li::before{content:"";position:absolute;left:1px;top:6px;width:4px;height:4px;border-radius:50%;background:var(--red)}
  .points{position:absolute;left:475px;top:598px;width:298px}
  .point{position:relative}
  .point::before{content:"";position:absolute;left:-25px;top:9px;width:11px;height:11px;border-radius:50%;background:var(--red)}
  .point-head{font-size:21px;line-height:1.2}
  .point-small{font-size:13.6px;line-height:1.2}
  .notice{font-size:38px;font-weight:700;color:var(--navy);line-height:1.1;margin-bottom:12px}
  .point-body{font-size:21px;line-height:26px;text-align:justify}
  .hl{color:var(--red);font-weight:700}
  .contact{position:absolute;left:55px;top:1033px;list-style:none;color:#fff}
  .contact li{font-size:16px;line-height:20.5px;display:flex;align-items:center;gap:8px}
  .contact svg{position:static;width:10px;height:10px;fill:#fff}
</style>
</head>
<body>
<main class="flyer">
  <svg width="820" height="1150" viewBox="0 0 820 1150">
    <defs>
      <linearGradient id="photoTone" x1="0" y1="0" x2="0" y2="1">
        <stop offset="0" stop-color="#c9d6e3"/>
        <stop offset=".35" stop-color="#d9b27a"/>
        <stop offset=".7" stop-color="#c79a5e"/>
        <stop offset="1" stop-color="#8d8a6e"/>
      </linearGradient>
      <linearGradient id="mistTone" x1="0" y1="0" x2="1" y2="1">
        <stop offset="0" stop-color="#ffffff"/>
        <stop offset="1" stop-color="#e3e6ea"/>
      </linearGradient>
      <linearGradient id="bandTone" x1="0" y1="0" x2="0" y2="1">
        <stop offset="0" stop-color="var(--blue)"/>
        <stop offset="1" stop-color="var(--blue-deep)"/>
      </linearGradient>
    </defs>
    <path role="img" aria-label="faint photo of hands cleaning a surface" d="M820,405 C650,440 460,560 260,585 L330,900 L820,720 Z" fill="url(#mistTone)"/>
    <path role="img" aria-label="photo of a timber house under renovation with scaffolding" d="M0,200 C80,245 160,262 260,238 C430,196 610,110 820,118 L820,408 C650,430 450,560 262,582 C150,594 60,565 0,512 Z" fill="url(#photoTone)"/>
    <path d="M0,200 C80,245 160,262 260,238 C430,196 610,110 820,118" fill="none" stroke="var(--navy)" stroke-width="14"/>
    <path d="M0,214 C80,259 160,276 260,252 C430,210 610,124 820,132" fill="none" stroke="var(--red)" stroke-width="4"/>
    <path d="M0,188 C80,232 160,250 260,226 C430,184 610,102 820,108" fill="none" stroke="var(--red)" stroke-width="3"/>
    <path d="M0,512 C60,565 150,594 262,582 C450,560 650,430 820,408" fill="none" stroke="var(--red)" stroke-width="16"/>
    <path d="M0,1030 C60,985 120,958 200,960 C330,964 450,1030 560,1080 L820,1150 L0,1150 Z" fill="url(#bandTone)"/>
    <path d="M0,1030 C60,985 120,958 200,960 C330,964 450,1030 560,1080 L820,1150" fill="none" stroke="var(--red)" stroke-width="7"/>
    <rect role="img" aria-label="photo of a smiling tradesman in a checked shirt, apron and tool belt" x="500" y="795" width="270" height="355" rx="60" fill="#7a8a9c" opacity=".85"/>
  </svg>

  <div class="brand">
    <span class="brand-dot"></span>
    <span class="brand-name">Swift Care Maintenance Solutions</span>
  </div>

  <section class="about">
    <h2>Swift Care Maintenance Solutions</h2>
    <p class="lead">is a commercial building and maintenance company established and located on the Sunshine Coast in QLD.</p>
    <p>We have expertise in retirement living and aged care maintenance works such as cleaning and painting programs, reinstatement works including painting and carpet replacement as well as major refurbishment or upgrade works including kitchen and bathroom works, electrical and air conditioning upgrade works.</p>
  </section>

  <section class="trades">
    <h3>Trades we specialise in:</h3>
    <ul>
      <li>Painting and building cleaning</li>
      <li>Carpentry and minor repairs</li>
      <li>Plastering and rendering</li>
      <li>Carpet and floor laying</li>
      <li>Electrical</li>
      <li>Plumbing</li>
      <li>Air conditioning upgrades</li>
    </ul>
  </section>

  <section class="points">
    <div class="point">
      <p class="point-head">We have the ability to react</p>
      <p class="point-small">quickly and complete works with as little as</p>
      <p class="notice">24 hours notice</p>
    </div>
    <div class="point">
      <p class="point-body">We are <span class="hl">licensed</span> and <span class="hl">insured</span>, and have a full workplace <span class="hl">health and safety compliance</span> system.</p>
    </div>
  </section>

  <ul class="contact">
    <li><svg viewBox="0 0 10 10"><path d="M2 0l2 2-1 1.5c.8 1.5 2 2.7 3.5 3.5L8 6l2 2-1.5 2C4 9.5.5 6 0 1.5z"/></svg>xxxxxxxxxx</li>
    <li><svg viewBox="0 0 10 10"><circle cx="5" cy="5" r="5"/></svg>www.swiftcaremaint.com.au</li>
    <li><svg viewBox="0 0 10 10"><path d="M0 2h10v6H0z"/></svg>hello@swiftcaremaint.com.au</li>
    <li><svg viewBox="0 0 10 10"><path d="M5 0a3.5 3.5 0 0 1 3.5 3.5C8.5 6 5 10 5 10S1.5 6 1.5 3.5A3.5 3.5 0 0 1 5 0z"/></svg>Lorem Ipsum is simply dummy text</li>
  </ul>
</main>
</body>
</html>
```